Sale Hang Tag

Design a bright, cheerful, compelling, call to action sale tag for a lighting showroom. The tag will be used to move older or discontinued product at a really good price. Upscale, friendly, neighbor store. Size should be no larger than 4 by 6 inches.

Call

```html
<!DOCTYPE html>
<html lang="en">
<head>
<meta charset="utf-8">
<title>Sale Hang Tag</title>
<link rel="stylesheet" href="https://fonts.googleapis.com/css2?family=Merriweather:ital,wght@1,700;1,900&display=swap">
<style>
  :root {
    --backdrop: #ededed;
    --tag-pink: #fe2558;
    --tag-amber: #ffaa00;
    --ink-white: #ffffff;
  }
  html, body {
    margin: 0;
    padding: 0;
    overflow: hidden;
  }
  body {
    width: 1200px;
    height: 1000px;
    background: var(--backdrop);
    position: relative;
    font-family: "Merriweather", Georgia, serif;
  }
  .hang-tag {
    position: absolute;
    width: 780px;
    height: 380px;
    border-radius: 32px;
    color: var(--ink-white);
  }
  .hang-tag--front { background: var(--tag-pink); left: 95px; top: 80px; }
  .hang-tag--back { background: var(--tag-amber); left: 320px; top: 475px; }
  .string-hole {
    position: absolute;
    left: 24px;
    top: 50%;
    width: 20px;
    height: 20px;
    margin-top: -10px;
    border-radius: 50%;
    background: var(--backdrop);
  }
  .tag-rule {
    position: absolute;
    left: 60px;
    right: 50px;
    margin: 0;
    display: flex;
    align-items: center;
    gap: 18px;
    font-style: italic;
    font-weight: 700;
    font-size: 27px;
    line-height: 1;
    white-space: nowrap;
  }
  .tag-rule--top { top: 46px; }
  .tag-rule--bottom { bottom: 46px; }
  .tag-rule::before,
  .tag-rule::after {
    content: "";
    flex: 1;
    height: 3px;
    background: radial-gradient(circle, var(--ink-white) 1.4px, transparent 1.7px) 0 0 / 10px 3px repeat-x;
  }
  .tag-rule--top::before { flex: 1; }
  .tag-rule--top::after { flex: 1.05; }
  .tag-rule--bottom::before { flex: 0.85; }
  .tag-rule--bottom::after { flex: 1; }
  .tag-headline {
    position: absolute;
    left: 40px;
    right: 30px;
    top: 88px;
    height: 210px;
    margin: 0;
    display: flex;
    align-items: center;
    justify-content: center;
    font-style: italic;
    font-weight: 700;
    font-size: 200px;
    line-height: 1;
    letter-spacing: -1px;
  }
</style>
</head>
<body>
  <article class="hang-tag hang-tag--front">
    <span class="string-hole"></span>
    <p class="tag-rule tag-rule--top">Upto 70% Off</p>
    <h1 class="tag-headline">Sale!</h1>
    <p class="tag-rule tag-rule--bottom">Limited Time Only</p>
  </article>

  <article class="hang-tag hang-tag--back">
    <span class="string-hole"></span>
    <p class="tag-rule tag-rule--top">Upto 70% Off</p>
    <h2 class="tag-headline">Sale!</h2>
    <p class="tag-rule tag-rule--bottom">Limited Time Only</p>
  </article>
</body>
</html>
```